Letterhead Design for Law Firm that Specializes in Property Damage Litigation

We are looking for a redesign of our letterhead. Our current letterhead lists all of our current staff members and we'd like to come up with a design that does NOT list all of the staff members so that it does not need to be updated with every newly hired employee. Must be in editable format.

We are a law firm that specializes in property damage, so we need something that is professional, yet modern. The final design should use our existing logo and should use a blue color scheme (alternate colors would be gray, black, and white).

Industry/Entity Type

Legal

Colors
0054AA
0677BA
7BADD7
CADEEF
E8F1F8

```html
<!DOCTYPE html>
<html lang="en">
<head>
<meta charset="utf-8">
<title>Hartwell Crane &amp; Osei — Letterhead</title>
<link rel="stylesheet" href="https://fonts.googleapis.com/css2?family=Crimson+Pro:wght@400;600&family=Source+Sans+3:wght@400;500&display=swap">
<style>
  :root {
    --navy: #1b2f66;
    --blue: #0a77ba;
    --ink: #222222;
    --body: #333333;
    --page-bg: #343a42;
    --paper: #ffffff;
  }
  * { margin: 0; padding: 0; box-sizing: border-box; }
  html, body { width: 1200px; height: 2486px; overflow: hidden; background: var(--page-bg); }
  body { position: relative; font-family: "Source Sans 3", Arial, sans-serif; }

  .letterhead {
    position: absolute;
    left: 199px; top: 1169px;
    width: 830px; height: 1075px;
    background: var(--paper);
    transform: scale(0.965);
    transform-origin: 0 0;
    overflow: hidden;
  }

  .firm-name {
    position: absolute; left: 97px; top: 136px;
    display: flex; align-items: center; gap: 14px;
    font-family: "Crimson Pro", Georgia, serif;
    font-weight: 600; font-size: 40px; line-height: 48px; letter-spacing: 1px;
    color: var(--navy);
    white-space: nowrap;
  }
  .firm-name .mark { width: 22px; height: 22px; background: var(--navy); }

  .office { position: absolute; top: 838px; width: 320px; }
  .office.nj { left: 98px; }
  .office.pa { left: 478px; }
  .office h2 {
    font-family: "Crimson Pro", Georgia, serif; font-weight: 400;
    font-size: 28px; color: var(--navy); line-height: 32px; margin-bottom: 6px;
    white-space: nowrap;
  }
  .contact { display: flex; gap: 6px; font-size: 15px; color: var(--body); line-height: 19px; margin-bottom: 11px; white-space: nowrap; }
  .contact svg { flex: 0 0 18px; margin-top: 1px; }

  .main-phone, .website {
    position: absolute; top: 992px; font-size: 16px; line-height: 20px; letter-spacing: 1.6px; color: var(--ink);
  }
  .main-phone { left: 97px; }
  .website { left: 478px; }

  .footer-band { position: absolute; left: 0; bottom: 0; width: 830px; height: 31px; }
</style>
</head>
<body>
  <main class="letterhead">
    <div class="firm-name"><span class="mark"></span>Hartwell Crane &amp; Osei</div>

    <section class="office nj">
      <h2>New Jersey Office</h2>
      <div class="contact">
        <svg width="18" height="18" viewBox="0 0 18 18"><circle cx="9" cy="9" r="9" fill="var(--navy)"/><path d="M6 4.5c.6-.3 1.1 0 1.4.6l.6 1.3c.2.5 0 .9-.4 1.2l-.4.3c.5 1.2 1.3 2 2.4 2.6l.4-.4c.3-.4.8-.5 1.2-.3l1.3.6c.6.3.8.9.5 1.4-.6 1.1-1.7 1.4-2.9.9C7.7 11.9 6 10.2 5.3 8c-.4-1.4 0-2.8.7-3.5z" fill="#fff"/></svg>
        856.555.0142
      </div>
      <div class="contact">
        <svg width="18" height="18" viewBox="0 0 18 18"><circle cx="9" cy="9" r="9" fill="var(--navy)"/><rect x="5" y="7" width="8" height="6" rx="1" fill="#fff"/><rect x="6.5" y="4.5" width="5" height="3" fill="#fff"/></svg>
        215.555.0190 0
      </div>
      <div class="contact">
        <svg width="18" height="18" viewBox="0 0 18 18"><circle cx="9" cy="9" r="9" fill="var(--blue)"/><path d="M9 3.5a3.6 3.6 0 0 0-3.6 3.6C5.4 10 9 14 9 14s3.6-4 3.6-6.9A3.6 3.6 0 0 0 9 3.5z" fill="#fff"/><circle cx="9" cy="7.2" r="1.4" fill="var(--blue)"/></svg>
        <span>300 Maple Avenue Suite<br>410 Haddon Park, NJ 08099</span>
      </div>
    </section>

    <section class="office pa">
      <h2>Philadelphia Office</h2>
      <div class="contact">
        <svg width="18" height="18" viewBox="0 0 18 18"><circle cx="9" cy="9" r="9" fill="var(--navy)"/><path d="M6 4.5c.6-.3 1.1 0 1.4.6l.6 1.3c.2.5 0 .9-.4 1.2l-.4.3c.5 1.2 1.3 2 2.4 2.6l.4-.4c.3-.4.8-.5 1.2-.3l1.3.6c.6.3.8.9.5 1.4-.6 1.1-1.7 1.4-2.9.9C7.7 11.9 6 10.2 5.3 8c-.4-1.4 0-2.8.7-3.5z" fill="#fff"/></svg>
        215.555.0100
      </div>
      <div class="contact">
        <svg width="18" height="18" viewBox="0 0 18 18"><circle cx="9" cy="9" r="9" fill="var(--navy)"/><rect x="5" y="7" width="8" height="6" rx="1" fill="#fff"/><rect x="6.5" y="4.5" width="5" height="3" fill="#fff"/></svg>
        215.555.0190
      </div>
      <div class="contact">
        <svg width="18" height="18" viewBox="0 0 18 18"><circle cx="9" cy="9" r="9" fill="var(--blue)"/><path d="M9 3.5a3.6 3.6 0 0 0-3.6 3.6C5.4 10 9 14 9 14s3.6-4 3.6-6.9A3.6 3.6 0 0 0 9 3.5z" fill="#fff"/><circle cx="9" cy="7.2" r="1.4" fill="var(--blue)"/></svg>
        <span>2200 Market Street Suite<br>900 Philadelphia, PA 19103</span>
      </div>
    </section>

    <div class="main-phone">(215) 555-0100</div>
    <div class="website">www.hcolegal.com</div>

    <svg class="footer-band" viewBox="0 0 830 31" preserveAspectRatio="none">
      <polygon points="0,0 402,0 391,31 0,31" fill="var(--blue)"/>
      <polygon points="408,0 830,0 830,31 397,31" fill="var(--navy)"/>
    </svg>
  </main>
</body>
</html>
```